Powerpoint Presentation Template

Kindly design a business class Powepoint Presentation template for our business use. Please stick to our company colours or even pictures as shown on our website and Logo

```html
<!DOCTYPE html>
<html lang="en">
<head>
<meta charset="utf-8">
<title>Veldmark Properties – Presentation Template</title>
<link href="https://fonts.googleapis.com/css2?family=Ubuntu:wght@300;400;500&family=Open+Sans:wght@400;600&display=swap" rel="stylesheet">
<style>
:root{
  --maroon:#8a1c17;
  --grey:#6d6e70;
  --line:#a7a8aa;
  --canvas:#e4e4e4;
  --slide:#ffffff;
  --panel:#d9d9d9;
  --sky:#9fb6cf;
  --earth:#b5652f;
  --dark:#3b3c40;
}
*{box-sizing:border-box;margin:0;padding:0}
html,body{width:872px;height:1200px;overflow:hidden;background:var(--canvas)}
body{position:relative;font-family:"Open Sans",sans-serif;color:var(--grey)}
.slide{position:absolute;width:368px;height:206px;background:var(--slide);box-shadow:0 2px 6px rgba(0,0,0,.35);overflow:hidden}
.slide > *{position:absolute}
.top-rule{top:0;left:20px;width:340px;height:1px;background:linear-gradient(90deg,var(--maroon),#d9a09c)}
.slide-title{left:19px;top:20px;font-family:"Ubuntu",sans-serif;font-size:11px;font-weight:400;color:var(--grey);letter-spacing:.2px}
.slide-title b{font-weight:500;color:var(--maroon)}
.title-rule{left:19px;top:35px;width:332px;height:1px;background:var(--line)}
.foot-line{left:0;bottom:6px;width:368px;height:1px;background:var(--line)}
.foot-band{right:0;bottom:5px;width:46px;height:5px;background:var(--maroon);clip-path:polygon(10% 0,100% 0,100% 100%,0 100%)}
.foot-brand{right:44px;bottom:9px;font-family:"Ubuntu",sans-serif;font-size:5px;font-weight:500;color:var(--maroon);text-align:center;line-height:1}
.ph{background:linear-gradient(180deg,var(--sky),#d7dde2 55%,var(--earth))}
.ph.building{background:linear-gradient(180deg,#8ea9c6,#5a4f4a 40%,#3a3c41 80%,#8b7b66)}
.ph.road{background:linear-gradient(180deg,#8fb0cf,#7d8a56 35%,#b5652f 65%,#c77a3d)}
.ph.office{background:linear-gradient(135deg,#eef2f5,#c9d2da 50%,#3a3f4a)}
.ph.tech{background:linear-gradient(135deg,#2f4a63,#8fa8bd 50%,#d9e2ea)}
.ph.house{background:linear-gradient(180deg,#a9bdd1,#d6d2cb 50%,#8d8a86)}
.ph.sign{background:linear-gradient(180deg,#9db06f,#d8d5cf 55%,#a7a39b)}
.body-s{font-size:4.4px;line-height:7px;color:var(--grey)}

/* cover */
.cover .brand{left:0;top:14px;width:368px;text-align:center;font-family:"Ubuntu",sans-serif;color:var(--maroon);font-weight:500;font-size:15px;line-height:1}
.cover .brand span{display:block;font-size:10px;color:#333;font-weight:400;margin-top:2px}
.cover .band{left:0;width:368px;height:4px;background:#c9c9cb}
.cover .headline{left:0;top:174px;width:368px;text-align:center;font-family:"Ubuntu",sans-serif;font-weight:300;font-size:13px;color:var(--maroon)}

/* toc */
.toc-item{width:110px;height:22px}
.toc-num{position:absolute;left:0;top:2px;width:16px;height:16px;border-radius:50%;background:var(--maroon);border:1.5px solid #d6b0ad;color:#fff;font-size:5px;display:flex;align-items:center;justify-content:center}
.toc-bar{position:absolute;left:20px;top:0;width:1px;height:20px;background:var(--maroon)}
.toc-head{position:absolute;left:24px;top:0;font-family:"Ubuntu",sans-serif;font-size:7.5px;color:var(--maroon)}
.toc-text{position:absolute;left:24px;top:10px;font-size:3.6px;line-height:5px;color:var(--grey);width:80px}

/* services */
.svc-icon{width:48px;height:48px}
.svc-text{width:74px;text-align:center}

/* who we are */
.who-col{width:68px}
.who-photo{position:absolute;left:13px;top:0;width:42px;height:42px;border-radius:50%;border:2px solid #5a8a4a}
.who-box{position:absolute;left:0;top:48px;width:68px;height:94px;background:var(--panel);padding:3px 4px}
.who-box h4{font-size:5px;line-height:6px;color:var(--maroon);font-weight:600}

/* two column */
.col-text{font-size:4.6px;line-height:8.2px;text-align:justify;color:#333}

/* closing */
.closing .shade{left:0;top:41px;width:368px;height:97px;background:rgba(20,20,25,.55)}
.contact{top:156px;font-size:5.5px;line-height:10px;color:#333}
.divider{top:156px;width:1px;height:20px;background:var(--maroon)}
.closing .brand{left:29px;top:156px;font-family:"Ubuntu",sans-serif;color:var(--maroon);font-weight:500;font-size:10px;line-height:1;text-align:center}
.closing .brand span{display:block;font-size:7px;color:#333;font-weight:400;margin-top:1px}
</style>
</head>
<body>

<!-- Slide 1: Cover -->
<section class="slide cover" style="left:57px;top:33px">
  <div class="brand">VELDMARK<span>Properties</span></div>
  <div class="band" style="top:49px"></div>
  <div class="ph road" style="left:0;top:58px;width:93px;height:35px" role="img" aria-label="Road construction site"></div>
  <div class="ph road" style="left:94px;top:58px;width:59px;height:35px" role="img" aria-label="Paved road through hills"></div>
  <div class="ph house" style="left:154px;top:58px;width:88px;height:35px" role="img" aria-label="Townhouse development"></div>
  <div class="ph building" style="left:260px;top:58px;width:108px;height:99px" role="img" aria-label="Modern apartment block at dusk"></div>
  <div class="ph building" style="left:0;top:94px;width:162px;height:63px;background:linear-gradient(180deg,#9ab6d3,#e6e3de 45%,#55575c 75%,#9b9487)" role="img" aria-label="Office complex"></div>
  <div class="ph sign" style="left:164px;top:94px;width:94px;height:63px" role="img" aria-label="Company entrance sign"></div>
  <div class="band" style="top:160px"></div>
  <div class="headline">YOUR HEADLINE TEXT</div>
</section>

<!-- Slide 2: Table of content -->
<section class="slide" style="left:451px;top:33px">
  <div class="slide-title">TABLE OF <b>CONTENT</b></div>
  <div class="title-rule" style="top:31px"></div>
  <div class="toc-item" style="left:19px;top:56px"><div class="toc-num">1</div><div class="toc-bar"></div><div class="toc-head">About Us</div><div class="toc-text">Lorem Ipsum is simply dummy text of the printing and typeset</div></div>
  <div class="toc-item" style="left:143px;top:56px"><div class="toc-num">2</div><div class="toc-bar"></div><div class="toc-head">Who We Are</div><div class="toc-text">Lorem Ipsum is simply dummy text of the printing and typeset</div></div>
  <div class="toc-item" style="left:262px;top:56px"><div class="toc-num">3</div><div class="toc-bar"></div><div class="toc-head">What We Do</div><div class="toc-text">Lorem Ipsum is simply dummy text of the printing and typeset</div></div>
  <div class="toc-item" style="left:19px;top:97px"><div class="toc-num">4</div><div class="toc-bar"></div><div class="toc-head">About Us</div><div class="toc-text">Lorem Ipsum is simply dummy text of the printing and typeset</div></div>
  <div class="toc-item" style="left:143px;top:97px"><div class="toc-num">5</div><div class="toc-bar"></div><div class="toc-head">About Us</div><div class="toc-text">Lorem Ipsum is simply dummy text of the printing and typeset</div></div>
  <div class="toc-item" style="left:262px;top:97px"><div class="toc-num">6</div><div class="toc-bar"></div><div class="toc-head">About Us</div><div class="toc-text">Lorem Ipsum is simply dummy text of the printing and typeset</div></div>
  <div class="toc-item" style="left:19px;top:143px"><div class="toc-num">7</div><div class="toc-bar"></div><div class="toc-head">About Us</div><div class="toc-text">Lorem Ipsum is simply dummy text of the printing and typeset</div></div>
  <div class="toc-item" style="left:143px;top:143px"><div class="toc-num">8</div><div class="toc-bar"></div><div class="toc-head">About Us</div><div class="toc-text">Lorem Ipsum is simply dummy text of the printing and typeset</div></div>
  <div class="toc-item" style="left:262px;top:143px"><div class="toc-num">9</div><div class="toc-bar"></div><div class="toc-head">About Us</div><div class="toc-text">Lorem Ipsum is simply dummy text of the printing and typeset</div></div>
  <div class="foot-line"></div><div class="foot-band"></div><div class="foot-brand">VELDMARK<br>Properties</div>
</section>

<!-- Slide 3: Our services -->
<section class="slide" style="left:57px;top:261px">
  <div class="top-rule"></div>
  <div class="slide-title">OUR <b>SERVICES</b></div>
  <div class="title-rule"></div>
  <svg class="svc-icon" style="left:34px;top:51px" viewBox="0 0 48 48" aria-hidden="true"><circle cx="24" cy="24" r="22.5" fill="#fff" stroke="#8a1c17" stroke-width="2"/><circle cx="24" cy="24" r="20" fill="#6d6e70"/><path d="M12 24l7-6 5 3 5-3 7 6-9 7-3-2-3 2z" fill="none" stroke="#fff" stroke-width="2" stroke-linejoin="round"/></svg>
  <svg class="svc-icon" style="left:115px;top:51px" viewBox="0 0 48 48" aria-hidden="true"><circle cx="24" cy="24" r="22.5" fill="#fff" stroke="#8a1c17" stroke-width="2"/><circle cx="24" cy="24" r="20" fill="#6d6e70"/><circle cx="24" cy="21" r="7" fill="#fff"/><path d="M13 36c2-6 6-8 11-8s9 2 11 8z" fill="#fff"/><path d="M15 22a9 9 0 0 1 18 0" fill="none" stroke="#fff" stroke-width="2"/></svg>
  <svg class="svc-icon" style="left:202px;top:51px" viewBox="0 0 48 48" aria-hidden="true"><circle cx="24" cy="24" r="22.5" fill="#fff" stroke="#8a1c17" stroke-width="2"/><circle cx="24" cy="24" r="20" fill="#6d6e70"/><rect x="16" y="12" width="17" height="23" rx="1.5" fill="none" stroke="#fff" stroke-width="2"/><path d="M20 18h9M20 22h9M20 26h5" stroke="#fff" stroke-width="1.6"/><path d="M14 29l3 3 5-6" fill="none" stroke="#fff" stroke-width="2"/></svg>
  <svg class="svc-icon" style="left:288px;top:51px" viewBox="0 0 48 48" aria-hidden="true"><circle cx="24" cy="24" r="22.5" fill="#fff" stroke="#8a1c17" stroke-width="2"/><circle cx="24" cy="24" r="20" fill="#6d6e70"/><path d="M13 34h22" stroke="#fff" stroke-width="2"/><rect x="15" y="25" width="4" height="8" fill="#fff"/><rect x="21" y="21" width="4" height="12" fill="#fff"/><rect x="27" y="17" width="4" height="16" fill="#fff"/><path d="M14 22l8-6 5 3 8-6" fill="none" stroke="#fff" stroke-width="1.6"/></svg>
  <p class="svc-text body-s" style="left:21px;top:105px">Lorem Ipsum is simply dummy text of the printing and typesetting industry. Lorem Ipsum has been Lorem Ipsum is simply dummy text of the printing and typesetting industry. Lorem Ipsum</p>
  <p class="svc-text body-s" style="left:102px;top:105px">Lorem Ipsum is simply dummy text of the printing and typesetting industry. Lorem Ipsum has been Lorem Ipsum is simply dummy text of the printing and typesetting industry. Lorem Ipsum</p>
  <p class="svc-text body-s" style="left:189px;top:105px">Lorem Ipsum is simply dummy text of the printing and typesetting industry. Lorem Ipsum has been Lorem Ipsum is simply dummy text of the printing and typesetting industry. Lorem Ipsum</p>
  <p class="svc-text body-s" style="left:275px;top:105px">Lorem Ipsum is simply dummy text of the printing and typesetting industry. Lorem Ipsum has been Lorem Ipsum is simply dummy text of the printing and typesetting industry. Lorem Ipsum</p>
  <div class="foot-line"></div><div class="foot-band"></div><div class="foot-brand">VELDMARK<br>Properties</div>
</section>

<!-- Slide 4: Who we are -->
<section class="slide" style="left:451px;top:261px">
  <div class="top-rule"></div>
  <div class="slide-title">WHO <b>WE ARE</b></div>
  <div class="title-rule"></div>
  <div class="who-col" style="left:27px;top:37px"><div class="who-photo ph office" role="img" aria-label="Team member portrait"></div><div class="who-box"><h4>Lorem ipsum dolor sit amet, consecte-</h4><p class="body-s">Lorem Ipsum is simply dummy text of the printing and typesetting industry. Lorem Ipsum has been the industry's standard dummy text ever since the 1500s, when an unknown printer took a galley of type and scrambled it to</p></div></div>
  <div class="who-col" style="left:112px;top:37px"><div class="who-photo ph office" role="img" aria-label="Team member portrait"></div><div class="who-box"><h4>Lorem ipsum dolor sit amet, consecte-</h4><p class="body-s">Lorem Ipsum is simply dummy text of the printing and typesetting industry. Lorem Ipsum has been the industry's standard dummy text ever since the 1500s, when an unknown printer took a galley of type and scrambled it to</p></div></div>
  <div class="who-col" style="left:197px;top:37px"><div class="who-photo ph office" role="img" aria-label="Team member portrait"></div><div class="who-box"><h4>Lorem ipsum dolor sit amet, consecte-</h4><p class="body-s">Lorem Ipsum is simply dummy text of the printing and typesetting industry. Lorem Ipsum has been the industry's standard dummy text ever since the 1500s, when an unknown printer took a galley of type and scrambled it to</p></div></div>
  <div class="who-col" style="left:282px;top:37px"><div class="who-photo ph office" role="img" aria-label="Team member portrait"></div><div class="who-box"><h4>Lorem ipsum dolor sit amet, consecte-</h4><p class="body-s">Lorem Ipsum is simply dummy text of the printing and typesetting industry. Lorem Ipsum has been the industry's standard dummy text ever since the 1500s, when an unknown printer took a galley of type and scrambled it to</p></div></div>
  <div class="foot-line"></div><div class="foot-band"></div><div class="foot-brand">VELDMARK<br>Properties</div>
</section>

<!-- Slide 5: Picture gallery -->
<section class="slide" style="left:57px;top:488px">
  <div class="top-rule"></div>
  <div class="slide-title">PICTURE <b>GALLERY</b></div>
  <div class="title-rule"></div>
  <div class="ph office" style="left:19px;top:40px;width:140px;height:138px" role="img" aria-label="Businessman relaxing at desk"></div>
  <div class="ph building" style="left:168px;top:40px;width:183px;height:68px;background:linear-gradient(180deg,#9ab6d3,#e6e3de 45%,#55575c 75%,#9b9487)" role="img" aria-label="Office complex"></div>
  <div class="ph road" style="left:168px;top:120px;width:90px;height:58px" role="img" aria-label="Road construction site"></div>
  <div class="ph house" style="left:263px;top:120px;width:88px;height:58px" role="img" aria-label="Townhouse development"></div>
  <div class="foot-line"></div><div class="foot-band"></div><div class="foot-brand">VELDMARK<br>Properties</div>
</section>

<!-- Slide 6: Picture description -->
<section class="slide" style="left:451px;top:488px">
  <div class="top-rule"></div>
  <div class="slide-title">PICTURE <b>DESCRIPTION</b></div>
  <div class="title-rule"></div>
  <div class="ph tech" style="left:19px;top:40px;width:175px;height:94px" role="img" aria-label="Hand drawing a cloud network diagram"></div>
  <div class="ph office" style="left:205px;top:40px;width:145px;height:94px" role="img" aria-label="Businessman relaxing at desk"></div>
  <p class="body-s" style="left:19px;top:144px;width:175px;font-size:4.5px">Lorem Ipsum is simply dummy text of the printing and typesetting industry. Lorem Ipsum has been the industry's standard dummy text ever since the 1500s, when an unknown printer took a galley of type and scrambled it to make a type specimen book. It has survived not</p>
  <p class="body-s" style="left:205px;top:144px;width:145px;font-size:4.5px">Lorem Ipsum is simply dummy text of the printing and typesetting industry. Lorem Ipsum has been the industry's standard dummy text ever since the 1500s, when an unknown printer took a galley of type and scrambled it to</p>
  <div class="foot-line"></div><div class="foot-band"></div><div class="foot-brand">VELDMARK<br>Properties</div>
</section>

<!-- Slide 7: Picture gallery -->
<section class="slide" style="left:57px;top:716px">
  <div class="slide-title">PICTURE <b>GALLERY</b></div>
  <div class="title-rule"></div>
  <div class="ph road" style="left:19px;top:40px;width:332px;height:62px" role="img" aria-label="Road construction with barriers"></div>
  <div class="ph building" style="left:18px;top:110px;width:106px;height:68px" role="img" aria-label="Modern apartment block at dusk"></div>
  <div class="ph sign" style="left:131px;top:110px;width:107px;height:68px" role="img" aria-label="Company entrance sign"></div>
  <div class="ph road" style="left:244px;top:110px;width:107px;height:68px;background:linear-gradient(180deg,#8fb0cf,#7d8a56 40%,#6f6f70 70%,#8b8b8b)" role="img" aria-label="Paved road through hills"></div>
  <div class="foot-line"></div><div class="foot-band"></div><div class="foot-brand">VELDMARK<br>Properties</div>
</section>

<!-- Slide 8: Two column pic text -->
<section class="slide" style="left:451px;top:716px">
  <div class="slide-title">TWO COLUMN <b>PIC TEXT</b></div>
  <div class="title-rule"></div>
  <div class="ph building" style="left:19px;top:42px;width:168px;height:136px" role="img" aria-label="Modern apartment block at dusk"></div>
  <div class="col-text" style="left:201px;top:38px;width:149px">
    <p>Lorem Ipsum is simply dummy text of the printing and typesetting industry. Lorem Ipsum has been the industry's standard dummy text ever since the 1500s, when an unknown printer took a galley of type and scrambled it to make a type specimen book. It has survived not only five centuries, but also the leap into electronic typesetting, remaining essentially unchanged. It was popularised in the 1960s with the release of Letraset sheets containing Lorem Ipsum passages, and more recently with desktop publishing software like Aldus PageMaker including versions of Lorem Ipsum.</p>
    <p style="margin-top:8px">It is a long established fact that a reader will be distracted by the readable content of a page when looking at its layout. The point of using Lorem Ipsum is that it has a more-or-less normal distribution of</p>
  </div>
  <div class="foot-line"></div><div class="foot-band"></div><div class="foot-brand">VELDMARK<br>Properties</div>
</section>

<!-- Slide 9: Closing -->
<section class="slide closing" style="left:57px;top:943px">
  <div class="ph road" style="left:0;top:41px;width:93px;height:35px" role="img" aria-label="Road construction site"></div>
  <div class="ph road" style="left:94px;top:41px;width:59px;height:35px" role="img" aria-label="Paved road through hills"></div>
  <div class="ph house" style="left:154px;top:41px;width:88px;height:35px" role="img" aria-label="Townhouse development"></div>
  <div class="ph building" style="left:260px;top:41px;width:108px;height:97px" role="img" aria-label="Modern apartment block at dusk"></div>
  <div class="ph building" style="left:0;top:77px;width:162px;height:61px;background:linear-gradient(180deg,#9ab6d3,#e6e3de 45%,#55575c 75%,#9b9487)" role="img" aria-label="Office complex"></div>
  <div class="ph sign" style="left:164px;top:77px;width:94px;height:61px" role="img" aria-label="Company entrance sign"></div>
  <div class="shade"></div>
  <div class="brand">VELDMARK<span>Properties</span></div>
  <div class="contact" style="left:98px">P: +00 555 010 2040<br>F: +00 555 010 2041</div>
  <div class="divider" style="left:167px"></div>
  <div class="contact" style="left:178px">info@veldmark.example<br>www.veldmark.example</div>
  <div class="divider" style="left:267px"></div>
  <div class="contact" style="left:277px">P.O. Box 1024, Eastvale<br>Region 7990, XX</div>
</section>

</body>
</html>
```